Web design concept for a IT recruitment agency.

Our website addresses two different target groups:
- Customers (companies) wanting to hire new IT talent
- It talent to find a new JOB

We a looking for a visual design concept that either addresses both target groups in one of the following options:
a. target both groups in 1 single splash page.
b. target both groups in 2 different pages one for both groups
c. or any creative third concept you can come up with

Requirements, we want one overall visual concept, that both target groups can relate to.

Trigger words what we want to express:
- passion / drive
- knowhow
- involvement
- professional/yet playful
- engagement

Background, company culture:
We are a recruitment agency with over 15 years of experience, we have no hard-sale culture.
But we emphasize on long term relationships, showing real interest in people and their needs.

Design requirements:
Use logo
Flat contemporary design

Target Market(s)

Industry/Entity Type

Hire

Number of Pages Required

2 page

Requirements
Must have
• We a looking for a visual design concept that either addresses both target groups

```html
<!DOCTYPE html>
<html lang="en">
<head>
<meta charset="utf-8">
<title>Hireloop – Looking for a job?</title>
<link href="https://fonts.googleapis.com/css2?family=Barlow:wght@300;400;500;600&display=swap" rel="stylesheet">
<style>
:root{
  --blue:#00a9ec;
  --blue-dark:#0092cf;
  --ink:#2f3438;
  --text:#5b6066;
  --muted:#9aa1a8;
  --line:#e3e7ea;
  --pale:#eef5fb;
  --dark:#1f2328;
  --white:#ffffff;
  --red:#e8442e;
  --green:#7cc243;
  --navy:#2c3e55;
}
*{box-sizing:border-box;margin:0;padding:0}
html,body{width:1200px;height:3141px;overflow:hidden}
body{position:relative;background:var(--white);font-family:"Barlow",Arial,sans-serif;color:var(--text)}
.abs{position:absolute}
a{color:inherit;text-decoration:none}

/* header */
.topbar{left:314px;top:0;width:886px;height:38px;background:var(--dark);clip-path:polygon(22px 0,100% 0,100% 100%,0 100%)}
.topbar-item{position:absolute;top:11px;font-size:13px;color:#d7dbdf;display:flex;align-items:center;gap:8px}
.topbar-item svg{width:14px;height:14px}
.login{position:absolute;right:98px;top:5px;width:76px;height:28px;border:1px solid var(--blue);color:#fff;font-size:12px;text-align:center;line-height:26px;letter-spacing:1px}
.signup{position:absolute;right:200px;top:11px;font-size:12px;color:#fff;letter-spacing:1px}
.brand{display:flex;align-items:center;gap:10px;font-size:32px;font-weight:500;color:var(--ink)}
.brand-dot{width:22px;height:22px;border-radius:50%;background:var(--blue)}
.nav{left:528px;top:38px;height:52px;display:flex}
.nav a{font-size:13px;font-weight:500;letter-spacing:1px;color:var(--ink);padding:0 16px;line-height:52px}
.nav a.active{background:var(--blue);color:#fff}

/* hero */
.hero{left:0;top:90px;width:1200px;height:580px;background:radial-gradient(ellipse at 50% 40%,#6b5a4a 0%,#3c342d 55%,#25211e 100%)}
.hero-title{left:0;top:316px;width:1200px;text-align:center;font-size:42px;font-weight:600;letter-spacing:10px;color:#fff}
.search{left:157px;top:398px;width:884px;height:117px;background:#fff;padding:18px 28px}
.search-lead{text-align:center;font-size:17px;color:var(--text)}
.search-lead b{color:var(--blue);font-weight:400}
.search-row{display:flex;gap:26px;margin-top:16px}
.field{height:42px;border:1px solid var(--line);font-size:13px;color:var(--muted);padding:0 14px;display:flex;align-items:center;justify-content:space-between;width:316px}
.btn{background:var(--blue);color:#fff;font-size:13px;font-weight:500;letter-spacing:1px;display:flex;align-items:center;justify-content:center}

/* process */
.eyebrow{font-size:15px;color:var(--blue);letter-spacing:2px;text-align:center}
.section-title{font-size:26px;font-weight:300;letter-spacing:4px;color:var(--ink);text-align:center}
.step{top:844px;width:316px;height:306px;text-align:center;padding-top:48px;border-bottom:3px solid var(--blue)}
.step.featured{background:var(--blue);color:#fff;border-bottom:none}
.step-icon{width:78px;height:78px;border-radius:50%;margin:0 auto;display:flex;align-items:center;justify-content:center}
.step h3{font-size:17px;font-weight:500;letter-spacing:2px;color:var(--ink);margin-top:34px}
.step.featured h3{color:#fff}
.step p{font-size:14px;line-height:21px;color:var(--muted);margin:12px auto 0;width:260px}
.step.featured p{color:#eaf7fd}

/* how it works */
.how{left:0;top:1250px;width:599px;height:385px;background:var(--pale);padding:70px 98px 0}
.how h2{font-size:19px;font-weight:400;letter-spacing:1px;color:var(--ink)}
.how p{font-size:13.5px;line-height:22px;color:var(--muted);margin-top:14px;width:420px}
.how .btn{width:146px;height:42px;margin-top:26px}
.video{left:599px;top:1250px;width:601px;height:385px;background:linear-gradient(120deg,#3d4a57 0%,#6a7580 45%,#c9cdd0 100%)}
.play{left:872px;top:1416px;width:52px;height:52px;border:3px solid #fff;border-radius:50%}

/* profiles */
.kicker{font-size:12px;color:var(--ink)}
.block-title{font-size:21px;font-weight:300;color:var(--ink)}
.table{left:157px;top:1792px;width:627px;height:507px;border:1px solid var(--line)}
.row{height:84px;border-bottom:1px solid var(--line);display:flex;align-items:center;padding:0 24px;font-size:13px;color:var(--text)}
.row:last-child{border-bottom:none}
.avatar{width:40px;height:40px;border-radius:50%;background:linear-gradient(135deg,#c98f70,#6b4636)}
.who{width:158px;margin-left:18px}
.who b{display:block;font-size:16px;font-weight:400;color:var(--ink)}
.who span{font-size:12px;color:var(--muted)}
.rate{width:66px}.type{width:86px}.loc{width:118px}
.view{width:88px;height:24px;border:1px solid var(--blue);color:var(--blue);font-size:12px;text-align:center;line-height:22px}
.team{left:844px;width:197px;border:1px solid var(--line)}
.team-img{height:192px;display:flex;flex-direction:column;align-items:center;justify-content:center;color:#fff;font-size:16px;gap:10px}
.team-img i{width:34px;height:34px;border-radius:50%;background:#fff;opacity:.9}
.team-meta{height:44px;display:flex;gap:26px;padding-left:24px;align-items:center;font-size:12px;color:var(--muted)}
.team-meta b{color:var(--blue);font-weight:400}

/* testimonial */
.quote-band{left:0;top:2383px;width:1200px;height:408px;background:linear-gradient(90deg,#2b2a29 0%,#4b4741 50%,#2e2d2c 100%)}
.quote-card{left:442px;top:2527px;width:314px;height:264px;background:#fff;padding:30px 34px}
.quote-card p{font-size:14px;line-height:22px;color:var(--text)}
.quote-card h4{font-size:16px;font-weight:400;color:var(--ink);margin-top:14px}
.quote-card small{font-size:12px;color:var(--blue)}
.quote-mark{left:422px;top:2505px;width:56px;height:56px;border-radius:50%;background:#fff;color:var(--muted);font-size:34px;text-align:center;line-height:64px;box-shadow:0 1px 4px rgba(0,0,0,.15)}
.dots{display:flex;gap:30px;justify-content:center;margin-top:24px}
.dots i{width:9px;height:9px;border-radius:50%;background:#d6dadd}
.dots i.on{background:var(--blue)}

/* footer */
.footer-label{font-size:12px;color:var(--muted)}
.subscribe{left:98px;top:2957px;display:flex}
.subscribe .input{width:200px;height:42px;background:#e9ecee;font-size:13px;color:var(--muted);padding:0 14px;line-height:42px}
.subscribe .btn{width:100px;height:42px}
.social{left:98px;top:3024px;display:flex;gap:24px}
.social i{width:14px;height:14px;border-radius:50%;background:#a9afb5}
.copy{left:98px;top:3070px;font-size:11px;color:var(--muted);letter-spacing:.5px}
.foot-title{font-size:18px;font-weight:400;color:var(--ink)}
.links{font-size:13px;color:var(--muted);line-height:22px}
.post{font-size:12px;line-height:18px;color:var(--muted);width:230px}
.post b{display:block;color:var(--ink);font-weight:400;margin-top:2px}
</style>
</head>
<body>

<!-- Header -->
<header>
  <div class="abs topbar">
    <div class="topbar-item" style="left:126px">
      <svg viewBox="0 0 14 14"><rect x="1" y="3" width="12" height="8" fill="none" stroke="#00a9ec" stroke-width="1.4"/><path d="M1 3l6 5 6-5" fill="none" stroke="#00a9ec" stroke-width="1.4"/></svg>
      mail@hireloop.example
    </div>
    <div class="topbar-item" style="left:330px">
      <svg viewBox="0 0 14 14"><path d="M3 1l3 3-2 2c1 2 2 3 4 4l2-2 3 3-2 2C6 12 2 8 1 3z" fill="#00a9ec"/></svg>
      CALL US : +49 (0)30 / 5550100-0
    </div>
    <a class="signup" href="#">SIGN UP</a>
    <a class="login" href="#">LOG IN</a>
  </div>
  <div class="abs brand" style="left:104px;top:22px"><span class="brand-dot"></span>Hireloop</div>
  <nav class="abs nav">
    <a class="active" href="#">HOME</a><a href="#">JOBS</a><a href="#">ADD A JOB</a><a href="#">CANDIDATES</a><a href="#">ADD A RESUME</a><a href="#">PAGES</a><a href="#">BLOG</a>
  </nav>
</header>

<!-- Hero -->
<section>
  <div class="abs hero" role="img" aria-label="Top-down photo of colleagues working with laptops and coffee at a wooden table"></div>
  <h1 class="abs hero-title">LOOKING FOR A JOB?</h1>
  <div class="abs search">
    <p class="search-lead">We've over <b>15 000 job</b> offers for you!</p>
    <div class="search-row">
      <div class="field">keywords (Skills, Services)<span>▾</span></div>
      <div class="field">location (State, City)<span>▾</span></div>
      <div class="btn" style="width:146px;height:42px">QUICK SEARCH</div>
    </div>
  </div>
</section>

<!-- Process -->
<section>
  <p class="abs eyebrow" style="left:0;top:742px;width:1200px">OUR PROCESS</p>
  <h2 class="abs section-title" style="left:0;top:764px;width:1200px">HOW WE WORK FOR YOU?</h2>

  <div class="abs step" style="left:98px">
    <div class="step-icon" style="background:var(--red)">
      <svg width="44" height="44" viewBox="0 0 44 44"><circle cx="22" cy="22" r="17" fill="#fff"/><text x="22" y="30" text-anchor="middle" font-family="Barlow,sans-serif" font-size="22" font-weight="600" fill="#2a6fb0">?</text></svg>
    </div>
    <h3>SEARCH THE BEST JOB</h3>
    <p>Find open roles that fit your skills, your pace and the way you like to work with teams.</p>
  </div>
  <div class="abs step featured" style="left:442px">
    <div class="step-icon" style="background:#fff">
      <svg width="40" height="40" viewBox="0 0 40 40"><rect x="8" y="6" width="18" height="24" fill="#5aa232"/><rect x="14" y="11" width="18" height="24" fill="var(--green)"/></svg>
    </div>
    <h3>CREATE YOUR RESUME</h3>
    <p>Build a clear profile in minutes and show what you know, what you love and where you grow.</p>
  </div>
  <div class="abs step" style="left:783px">
    <div class="step-icon" style="background:var(--navy)">
      <svg width="40" height="40" viewBox="0 0 40 40"><circle cx="20" cy="15" r="7" fill="#f1c9a5"/><path d="M8 36c0-8 5-12 12-12s12 4 12 12z" fill="#e8442e"/></svg>
    </div>
    <h3>FACE INTERVIEW ONLINE</h3>
    <p>Meet hiring teams by video call and talk openly about the role, the people and the goals.</p>
  </div>
</section>

<!-- How it works -->
<section>
  <div class="abs how">
    <h2>HOW DOES IT WORK</h2>
    <p>We listen first. Tell us what drives you and what you need, and we match you with companies that share your way of working. No hard sale, just honest advice and a long relationship built on real interest in people, their skills and their plans for the years ahead.</p>
    <div class="btn">QUICK SEARCH</div>
  </div>
  <div class="abs video" role="img" aria-label="Video still of a person writing notes in a notebook beside a laptop"></div>
  <svg class="abs" style="left:593px;top:1434px" width="12" height="16" viewBox="0 0 12 16"><path d="M0 0l12 8-12 8z" fill="#eef5fb"/></svg>
  <div class="abs play"></div>
  <svg class="abs" style="left:892px;top:1431px" width="18" height="22" viewBox="0 0 18 22"><path d="M0 0l18 11L0 22z" fill="#fff"/></svg>
</section>

<!-- Profiles & teams -->
<section>
  <p class="abs kicker" style="left:157px;top:1718px">Top workers at present</p>
  <h2 class="abs block-title" style="left:157px;top:1734px">Featured Profiles</h2>
  <p class="abs kicker" style="left:672px;top:1748px"><span style="color:var(--blue)">2,400</span> Active Profiles</p>

  <div class="abs table">
    <div class="row"><i class="avatar" role="img" aria-label="Profile photo"></i><div class="who"><b>Tavi Renner</b><span>Marketing Expert</span></div><span class="rate">$45/hr</span><span class="type">Full Time</span><span class="loc">California, USA</span><a class="view" href="#">View Profile</a></div>
    <div class="row"><i class="avatar" role="img" aria-label="Profile photo"></i><div class="who"><b>Lena Hartwig</b><span>Ux Designer</span></div><span class="rate">$45/hr</span><span class="type">Full Time</span><span class="loc">California, USA</span><a class="view" href="#">View Profile</a></div>
    <div class="row"><i class="avatar" role="img" aria-label="Profile photo" style="background:linear-gradient(135deg,#bbb,#555)"></i><div class="who"><b>Oskar Vial</b><span>Developer</span></div><span class="rate">$45/hr</span><span class="type">Full Time</span><span class="loc">California, USA</span><a class="view" href="#">View Profile</a></div>
    <div class="row"><i class="avatar" role="img" aria-label="Profile photo"></i><div class="who"><b>Marco Feld</b><span>SEO Expert</span></div><span class="rate">$45/hr</span><span class="type">Full Time</span><span class="loc">California, USA</span><a class="view" href="#">View Profile</a></div>
    <div class="row"><i class="avatar" role="img" aria-label="Profile photo"></i><div class="who"><b>Ida Sunbeck</b><span>Illustrator</span></div><span class="rate">$45/hr</span><span class="type">Full Time</span><span class="loc">California, USA</span><a class="view" href="#">View Profile</a></div>
    <div class="row"><i class="avatar" role="img" aria-label="Profile photo" style="background:linear-gradient(135deg,#e86a5a,#8a3a30)"></i><div class="who"><b>Runa Maas</b><span>Housewife</span></div><span class="rate">$45/hr</span><span class="type">Full Time</span><span class="loc">California, USA</span><a class="view" href="#">View Profile</a></div>
  </div>

  <p class="abs kicker" style="left:844px;top:1718px">Top teams at present</p>
  <h2 class="abs block-title" style="left:844px;top:1734px">Featured Teams</h2>
  <div class="abs team" style="top:1792px">
    <div class="team-img" role="img" aria-label="Team photo of a busy office" style="background:linear-gradient(160deg,#4d6f8e,#2c3a4a)"><i></i>Brightfold</div>
    <div class="team-meta"><b>Full Time</b>California, USA</div>
  </div>
  <div class="abs team" style="top:2062px">
    <div class="team-img" role="img" aria-label="Team photo of a warm-lit workspace" style="background:linear-gradient(160deg,#6a5a48,#2f2a25)"><i></i>Northpane</div>
    <div class="team-meta"><b>Part Time</b>California, USA</div>
  </div>
</section>

<!-- Testimonial -->
<section>
  <div class="abs quote-band" role="img" aria-label="Dimmed photo of people working in a cafe"></div>
  <div class="abs quote-card">
    <p>Got some real professional workers at reasonable price from remoteworkers website. Specially the designer has provided a great service. Thanks!</p>
    <h4>Peter Alswin</h4>
    <small>CEO Gridworks</small>
    <div class="dots"><i class="on"></i><i></i><i></i><i></i><i></i></div>
  </div>
  <div class="abs quote-mark">“</div>
</section>

<!-- Footer -->
<footer>
  <div class="abs brand" style="left:100px;top:2850px;font-size:30px"><span class="brand-dot"></span>Hireloop</div>
  <p class="abs footer-label" style="left:98px;top:2930px">Subscribe to our newsletter</p>
  <div class="abs subscribe"><div class="input">Your email</div><div class="btn">Subscribe</div></div>
  <div class="abs social" aria-label="Social links"><i></i><i></i><i></i><i></i><i></i><i></i></div>
  <p class="abs copy">©2015 Hireloop Talent - ALL RIGHTS RESERVED</p>

  <h3 class="abs foot-title" style="left:526px;top:2893px">Site Map</h3>
  <div class="abs links" style="left:526px;top:2929px">Our Blog<br>Company Directory<br>Contact Us<br>Find A Candidate</div>
  <div class="abs links" style="left:690px;top:2929px">Find A Job<br>Terms &amp; Conditions<br>Job Bookmarks<br>Plans &amp; Pricing</div>

  <h3 class="abs foot-title" style="left:869px;top:2893px">From Blog</h3>
  <div class="abs post" style="left:869px;top:2929px">Tech hiring keeps growing as teams in the UK and Ireland look for talent<b>July 22, 2013</b></div>
  <div class="abs post" style="left:869px;top:2998px">Remote roles change how developers pick their next employer and team<b>July 22, 2013</b></div>
</footer>

</body>
</html>
```